Premium men's gut health supplement needs a bottle label designed

We’re velnora - a premium men’s wellness brand focused on gut health. Our first product is a high-quality daily supplement designed to support digestion, regularity, and internal cleanliness. Backed by science and tailored for modern lifestyles, velnora is crafted in the UK and proudly LGBT-owned. It aims to resolve intimacy problems that gay men may experience due to poor digestion but also does not exclude any other orientation - other men may use it simply to improve their digestion.

velnora is for health-conscious men who value science-backed supplements and want to feel confident from the inside out. Many of our early adopters will be gay and bisexual men who prioritise gut health as part of their self-care, sexual, and hygiene routine, though the product is equally effective and appealing to anyone seeking premium digestive support.

The product is premium the target customer is male, not specific to one location but primary markets will be US, UK and EU.

I’d like a supplement bottle designed for velnora, our premium men’s gut health brand. The focus should be clean, slightly clinical, and minimal - inspired by brands like Quelrin and Darvo. The key element is the wordmark (velnora) on the front, with no additional logo or icon. Lowercase text and a strong, contemporary font are preferred.

The bottle should be aesthetically pleasing so that people are proud to display it on their shelf, instead of hiding it in a cupboard (like Quelrin, darvo, Pia Venturek, Morvanel etc)

Avoid anything that shows the product as being for LGBT, e.g., no rainbows, men holding hands etc.

The design should be premium, minimalist and not be busy or overwhelming.

I have uploaded a file called "Bottle" to give an idea of the type of container, but please ignore the colours and change as you see fit. This is just for reference for the type of bottle we'll use - all colours are customisable.

I have also uploaded some images for "style" reference, e.g., darvo, quelrin, pia venturek, etc for inspiration.

```html
<!DOCTYPE html>
<html lang="en">
<head>
<meta charset="UTF-8">
<title>velnora soltract label</title>
<link rel="stylesheet" href="https://fonts.googleapis.com/css2?family=DM+Serif+Display&family=Outfit:wght@400;600&display=swap">
<style>
  :root {
    --canvas-bg: #f4f4f3;
    --label-amber: #a6620c;
    --label-amber-light: #b5751f;
    --icon-tone: #c98c3a;
    --text-cream: #f5f0ea;
    --text-butter: #f8dc8c;
  }
  * { margin: 0; padding: 0; box-sizing: border-box; }
  html, body {
    width: 1200px;
    height: 1000px;
    overflow: hidden;
    background: var(--canvas-bg);
  }
  .canvas {
    position: relative;
    width: 1200px;
    height: 1000px;
  }
  .label {
    position: absolute;
    left: 320px;
    top: 114px;
    width: 560px;
    height: 772px;
    background: var(--label-amber);
    overflow: hidden;
    text-align: center;
  }
  .label__pattern {
    position: absolute;
    left: 10px;
    top: 0;
    width: 540px;
    height: 772px;
    background: radial-gradient(ellipse at 50% 55%, var(--label-amber-light) 0%, var(--label-amber) 72%);
    opacity: 0.55;
  }
  .wordmark {
    position: absolute;
    left: 0;
    right: 0;
    top: 88px;
    font-family: "DM Serif Display", Georgia, serif;
    font-weight: 400;
    font-size: 84px;
    line-height: 1;
    color: var(--text-cream);
    letter-spacing: 0.5px;
  }
  .label__icon {
    position: absolute;
    left: 252px;
    top: 278px;
    width: 56px;
    height: 90px;
    border-radius: 12px;
    background: var(--icon-tone);
    opacity: 0.6;
  }
  .product-name {
    position: absolute;
    left: 0;
    right: 0;
    top: 392px;
    font-family: "Outfit", Arial, sans-serif;
    font-weight: 600;
    font-size: 66px;
    line-height: 1;
    color: var(--text-cream);
    letter-spacing: 0.5px;
  }
  .product-type {
    position: absolute;
    left: 0;
    right: 0;
    top: 474px;
    font-family: "Outfit", Arial, sans-serif;
    font-weight: 400;
    font-size: 24px;
    line-height: 1;
    color: var(--text-butter);
  }
  .claims {
    position: absolute;
    left: 0;
    right: 0;
    top: 672px;
    font-family: "Outfit", Arial, sans-serif;
    font-weight: 400;
    font-size: 17px;
    line-height: 26px;
    color: var(--text-butter);
  }
</style>
</head>
<body>
<main class="canvas">
  <section class="label">
    <div class="label__pattern" role="img" aria-label="Large faint winding intestine line pattern running down the label"></div>
    <h1 class="wordmark">velnora</h1>
    <div class="label__icon" role="img" aria-label="Small outlined intestine icon"></div>
    <h2 class="product-name">soltract</h2>
    <p class="product-type">digestion supplement</p>
    <p class="claims">high-quality daily supplement<br>Backed by science and tailored for modern lifestyles</p>
  </section>
</main>
</body>
</html>
```